Bref créative
Stationary and Business Cards for property management company
Condo Managers
Simple
Owen R. Falk
P.O. Box 52947
LES DEUX RIVES
Brookvale, QC H3K 8T5
info@tidalnest.example
www.tidalnest.example
both the Stationary and Business cards will need to be adapted sing French at some point. Also he business card would be intended to have English on one side and the French equivalent on the other side. I can provide the French words when we get to that point.
[the French version]
English logo
logo French version

```html
<!DOCTYPE html>
<html lang="en">
<head>
<meta charset="utf-8">
<title>Tidalnest Stationery Set</title>
<link href="https://fonts.googleapis.com/css2?family=Raleway:wght@500&family=Open+Sans:wght@400;600&display=swap" rel="stylesheet">
<style>
:root{
  --backdrop:#8e9093;
  --paper:#ffffff;
  --ink:#4a4a4a;
  --muted:#9a9a9a;
  --brand-blue:#29abe2;
  --card-dark:#111214;
  --fade-blue:#d8eef9;
  --fade-green:#e6f2d4;
}
*{margin:0;padding:0;box-sizing:border-box}
html,body{width:1200px;height:758px;overflow:hidden;background:var(--backdrop)}
body{position:relative;font-family:"Open Sans",sans-serif;color:var(--ink)}
.set-row{position:absolute;left:0;width:1200px;height:379px}
.set-row.top{top:0}
.set-row.bottom{top:379px}
.sheet{position:absolute;background:var(--paper);overflow:hidden;box-shadow:0 1px 3px rgba(0,0,0,.25)}
.brand{font-family:"Raleway",sans-serif;font-weight:500;color:var(--brand-blue);letter-spacing:.04em;display:flex;align-items:center;gap:.35em;white-space:nowrap;line-height:1}
.brand .mark{width:.8em;height:.8em;background:var(--brand-blue);display:inline-block;flex:none}
.tagline{font-size:5px;letter-spacing:.25em;color:var(--muted);text-transform:uppercase;white-space:nowrap}
.fade-art{position:absolute;background:linear-gradient(160deg,var(--fade-blue),var(--fade-green));opacity:.7}
.edge-stripe{position:absolute;top:0;bottom:0;left:0;width:4px;background:var(--brand-blue)}
.contact{font-size:4px;line-height:1.5;color:var(--ink);white-space:nowrap}

.folder{left:0;top:5px;width:420px;height:367px;background:transparent;box-shadow:none;overflow:visible}
.folder-panel{position:absolute;top:0;height:100%;background:var(--paper);box-shadow:0 1px 3px rgba(0,0,0,.25);overflow:hidden}
.folder-panel.front{left:0;width:211px}
.folder-panel.inside{left:221px;width:199px}
.folder-spine{position:absolute;left:211px;top:0;width:10px;height:100%;background:var(--brand-blue)}
.folder-notch{position:absolute;left:196px;bottom:0}
.folder .front .brand{position:absolute;left:22px;top:134px;font-size:21px}
.folder .front .tagline{position:absolute;left:24px;top:160px}
.folder .front .foot-brand{position:absolute;left:62px;top:290px;font-size:9px}
.folder .inside .brand{position:absolute;left:22px;top:44px;font-size:11px}
.folder .inside .foot-brand{position:absolute;left:22px;top:300px;font-size:9px}

.notepad{left:432px;top:24px;width:91px;height:132px}
.notepad .brand{position:absolute;left:8px;top:10px;font-size:6px}
.memo{left:432px;top:163px;width:120px;height:200px}
.memo h2{position:absolute;left:8px;top:10px;font-size:6px;font-weight:600;letter-spacing:.15em}
.memo .fields{position:absolute;left:8px;top:24px;font-size:4px;line-height:2.2;color:var(--muted)}
.memo .brand{position:absolute;left:8px;bottom:10px;font-size:6px}
.slip{left:566px;top:36px;width:178px;height:80px}
.slip .brand{position:absolute;left:10px;top:10px;font-size:7px}
.slip .note{position:absolute;left:10px;top:30px;font-size:5px;font-style:italic;color:var(--muted)}
.slip .contact{position:absolute;left:10px;bottom:8px}
.letter{top:125px;width:190px;height:247px}
.letter.first{left:566px}
.letter.second{left:768px;top:96px;height:276px}
.letter .brand{position:absolute;left:14px;top:14px;font-size:8px}
.letter .contact{position:absolute;left:14px;bottom:8px}

.card{top:36px;width:86px;height:50px}
.card.light{left:773px}
.card.dark{background:var(--card-dark)}
.card.dark.one{left:869px}
.card.dark.two{left:970px}
.card .brand{position:absolute;left:6px;top:6px;font-size:6px}
.card .contact{position:absolute;left:6px;bottom:4px;font-size:3.2px}
.card.dark .contact{color:#cfd2d4}
.card.dark.one .contact{top:6px;bottom:auto}
.card.dark.two .brand{top:19px;left:14px;font-size:8px}

.envelope{left:970px;top:96px;width:230px;height:108px}
.envelope .brand{position:absolute;left:10px;top:10px;font-size:7px}
.envelope .contact{position:absolute;left:10px;top:22px}
.envelope-back{left:970px;top:211px;width:230px;height:100px}
.envelope-back svg{position:absolute;left:0;top:0}
</style>
</head>
<body>

<section class="set-row top">
  <div class="sheet folder">
    <div class="folder-panel front">
      <div class="brand"><span class="mark"></span>TIDALNEST</div>
      <div class="tagline">Condo Managers</div>
      <div class="brand foot-brand"><span class="mark"></span>TIDALNEST</div>
    </div>
    <div class="folder-spine"></div>
    <div class="folder-panel inside">
      <div class="brand"><span class="mark"></span>TIDALNEST</div>
      <div class="fade-art" style="left:80px;top:150px;width:110px;height:110px" role="img" aria-label="faint building motif"></div>
      <div class="brand foot-brand"><span class="mark"></span>TIDALNEST</div>
    </div>
    <svg class="folder-notch" width="40" height="72" viewBox="0 0 40 72"><polygon points="20,0 40,72 0,72" fill="var(--backdrop)"/></svg>
  </div>

  <div class="sheet notepad"><div class="brand"><span class="mark"></span>TIDALNEST</div><div class="fade-art" style="left:40px;top:70px;width:50px;height:60px" role="img" aria-label="faint building motif"></div></div>

  <div class="sheet memo">
    <h2>MEMO</h2>
    <div class="fields">To:<br>From:<br>Date:<br>Re:</div>
    <div class="fade-art" style="left:55px;top:120px;width:65px;height:80px" role="img" aria-label="faint building motif"></div>
    <div class="brand"><span class="mark"></span>TIDALNEST</div>
  </div>

  <div class="sheet slip">
    <div class="fade-art" style="left:120px;top:20px;width:55px;height:60px" role="img" aria-label="faint building motif"></div>
    <div class="brand"><span class="mark"></span>TIDALNEST</div>
    <div class="note">With compliments</div>
    <div class="contact">P.O. Box 31608, STATION NORDVAL, Brookvale, QC H3K 8T5</div>
  </div>

  <div class="sheet letter first">
    <div class="edge-stripe"></div>
    <div class="brand"><span class="mark"></span>TIDALNEST</div>
    <div class="fade-art" style="left:110px;top:160px;width:75px;height:75px" role="img" aria-label="faint building motif"></div>
    <div class="contact">P.O. Box 31608 · STATION NORDVAL · Brookvale, QC H3K 8T5 · www.tidalnest.example</div>
  </div>

  <div class="sheet letter second">
    <div class="edge-stripe"></div>
    <div class="brand"><span class="mark"></span>TIDALNEST</div>
    <div class="fade-art" style="left:110px;top:180px;width:78px;height:82px" role="img" aria-label="faint building motif"></div>
    <div class="contact">P.O. Box 31608 · STATION NORDVAL · Brookvale, QC H3K 8T5 · www.tidalnest.example</div>
  </div>

  <div class="sheet card light">
    <div class="brand"><span class="mark"></span>TIDALNEST</div>
    <div class="contact">Owen R. Falk<br>450-555-0142<br>info@tidalnest.example</div>
  </div>
  <div class="sheet card dark one">
    <div class="contact">Owen R. Falk<br>P.O. Box 31608<br>STATION NORDVAL<br>Brookvale, QC H3K 8T5<br>www.tidalnest.example</div>
  </div>
  <div class="sheet card dark two">
    <div class="brand"><span class="mark"></span>TIDALNEST</div>
  </div>

  <div class="sheet envelope">
    <div class="fade-art" style="left:170px;top:40px;width:55px;height:65px" role="img" aria-label="faint building motif"></div>
    <div class="brand"><span class="mark"></span>TIDALNEST</div>
    <div class="contact">P.O. Box 31608<br>STATION NORDVAL<br>Brookvale, QC H3K 8T5</div>
  </div>
  <div class="sheet envelope-back">
    <svg width="230" height="100" viewBox="0 0 230 100"><path d="M0 0 H230 L150 70 Q115 92 80 70 Z" fill="var(--card-dark)"/></svg>
  </div>
</section>

<section class="set-row bottom">
  <div class="sheet folder">
    <div class="folder-panel front">
      <div class="brand"><span class="mark"></span>TIDALNEST</div>
      <div class="tagline">Condo Managers</div>
      <div class="brand foot-brand"><span class="mark"></span>TIDALNEST</div>
    </div>
    <div class="folder-spine"></div>
    <div class="folder-panel inside">
      <div class="brand"><span class="mark"></span>TIDALNEST</div>
      <div class="fade-art" style="left:80px;top:150px;width:110px;height:110px" role="img" aria-label="faint building motif"></div>
      <div class="brand foot-brand"><span class="mark"></span>TIDALNEST</div>
    </div>
    <svg class="folder-notch" width="40" height="72" viewBox="0 0 40 72"><polygon points="20,0 40,72 0,72" fill="var(--backdrop)"/></svg>
  </div>

  <div class="sheet notepad"><div class="brand"><span class="mark"></span>TIDALNEST</div><div class="fade-art" style="left:40px;top:70px;width:50px;height:60px" role="img" aria-label="faint building motif"></div></div>

  <div class="sheet memo">
    <h2>MEMO</h2>
    <div class="fields">To:<br>From:<br>Date:<br>Re:</div>
    <div class="fade-art" style="left:55px;top:120px;width:65px;height:80px" role="img" aria-label="faint building motif"></div>
    <div class="brand"><span class="mark"></span>TIDALNEST</div>
  </div>

  <div class="sheet slip">
    <div class="fade-art" style="left:120px;top:20px;width:55px;height:60px" role="img" aria-label="faint building motif"></div>
    <div class="brand"><span class="mark"></span>TIDALNEST</div>
    <div class="note">With compliments</div>
    <div class="contact">P.O. Box 31608, STATION NORDVAL, Brookvale, QC H3K 8T5</div>
  </div>

  <div class="sheet letter first">
    <div class="edge-stripe"></div>
    <div class="brand"><span class="mark"></span>TIDALNEST</div>
    <div class="fade-art" style="left:110px;top:160px;width:75px;height:75px" role="img" aria-label="faint building motif"></div>
    <div class="contact">P.O. Box 31608 · STATION NORDVAL · Brookvale, QC H3K 8T5 · www.tidalnest.example</div>
  </div>

  <div class="sheet letter second">
    <div class="edge-stripe"></div>
    <div class="brand"><span class="mark"></span>TIDALNEST</div>
    <div class="fade-art" style="left:110px;top:180px;width:78px;height:82px" role="img" aria-label="faint building motif"></div>
    <div class="contact">P.O. Box 31608 · STATION NORDVAL · Brookvale, QC H3K 8T5 · www.tidalnest.example</div>
  </div>

  <div class="sheet card light">
    <div class="brand"><span class="mark"></span>TIDALNEST</div>
    <div class="contact">Owen R. Falk<br>450-555-0142<br>info@tidalnest.example</div>
  </div>
  <div class="sheet card dark one">
    <div class="contact">Owen R. Falk<br>P.O. Box 31608<br>STATION NORDVAL<br>Brookvale, QC H3K 8T5<br>www.tidalnest.example</div>
  </div>
  <div class="sheet card dark two">
    <div class="brand"><span class="mark"></span>TIDALNEST</div>
  </div>

  <div class="sheet envelope">
    <div class="fade-art" style="left:170px;top:40px;width:55px;height:65px" role="img" aria-label="faint building motif"></div>
    <div class="brand"><span class="mark"></span>TIDALNEST</div>
    <div class="contact">P.O. Box 31608<br>STATION NORDVAL<br>Brookvale, QC H3K 8T5</div>
  </div>
  <div class="sheet envelope-back">
    <svg width="230" height="100" viewBox="0 0 230 100"><path d="M0 0 H230 L150 70 Q115 92 80 70 Z" fill="var(--card-dark)"/></svg>
  </div>
</section>

</body>
</html>
```